Brightline Energy Product Distribution Brochure

We are looking to have our current brochure for our customers completely redesigned...the idea is to present the relevant information in an attractive way . Our website is brightlineenergyco.example where you can find more information about us. We have included a file with a rough idea of the page order and what each should include but feel free to adapt based on design. The example provided is only for context and doesnt have to be maintained. We will be using the brochure both digitally and in print form. As long as it reads easily and is eye catching, the design can be horizontal or vertical.Final deliverable should be indesign file.

"Our Brands" page: should be limited to one page (space being enough) where it has the header for each one (for example diesel generators) space for one or two lines of text and then the corresponding logos for each of the five categories
Updates

For those asking: the "our brands" page should be a single page layout where there is a header with the corresponding section and space for maybe one line of text followed by the two logos for that category. Each of the product pages should be similar in fashion to the one in the document attached: a photo of the product with some white space and space for the text to be included. We will be posting additional examples today

Target Market(s)

We want to present it to customers both digitally and in print so they can see our products

Industry/Entity Type

Power Generation

Font styles to use
Serif

Requirements
Must have
• Eye catching and able to present the information in a presentable fashion. Rest is up to you.
Nice to have
• Should incorporate the colors of our logo but can also add other depending on design

```html
<!DOCTYPE html>
<html lang="en">
<head>
<meta charset="utf-8">
<title>Brightline Energy — Index</title>
<link rel="stylesheet" href="https://fonts.googleapis.com/css2?family=Montserrat:wght@700&family=Raleway:wght@200;300;400&display=swap">
<style>
  :root {
    --bg-dark: #141414;
    --bg-mid: #272727;
    --yellow: #e1d431;
    --gold: #e8b41f;
    --gold-deep: #c9960f;
    --white: #ffffff;
    --ink: #1b1b1b;
    --soft: #ececec;
  }
  * { margin: 0; padding: 0; box-sizing: border-box; }
  html, body { width: 1200px; height: 934px; overflow: hidden; }
  body { font-family: 'Raleway', sans-serif; }
  .page {
    position: relative; width: 1200px; height: 934px; overflow: hidden;
    background: radial-gradient(ellipse at 45% 40%, var(--bg-mid) 0%, var(--bg-dark) 72%);
  }
  .corner-glow { position: absolute; pointer-events: none; }
  .corner-glow--top-right {
    right: 0; top: 0; width: 360px; height: 380px;
    background: radial-gradient(ellipse at 100% 0%, rgba(232,180,31,.75) 0%, rgba(232,180,31,.25) 45%, rgba(232,180,31,0) 72%);
  }
  .corner-glow--bottom-right {
    right: 0; bottom: 0; width: 380px; height: 420px;
    background: radial-gradient(ellipse at 100% 100%, rgba(232,180,31,.8) 0%, rgba(201,150,15,.3) 48%, rgba(201,150,15,0) 74%);
  }
  .corner-glow--bottom-left {
    left: 0; bottom: 60px; width: 160px; height: 160px;
    background: radial-gradient(ellipse at 0% 100%, rgba(232,180,31,.7) 0%, rgba(232,180,31,0) 70%);
  }
  .index-banner {
    position: absolute; left: 0; top: 38px; width: 371px; height: 100px;
    background: linear-gradient(90deg, var(--yellow), #d9cc2c);
    border-radius: 0 6px 6px 0;
    box-shadow: 0 6px 14px rgba(0,0,0,.5);
  }
  .index-banner h1 {
    position: absolute; left: 58px; top: 12px;
    font-family: 'Montserrat', sans-serif; font-weight: 700;
    font-size: 70px; letter-spacing: -1px; color: var(--ink); line-height: 76px;
  }
  .entry { position: absolute; width: 540px; height: 52px; }
  .entry .thumb {
    position: absolute; left: 0; top: 0; width: 222px; height: 52px;
    border: 2px solid var(--white); border-radius: 5px; overflow: hidden;
  }
  .entry .num {
    position: absolute; left: 12px; top: -4px;
    font-family: 'Raleway', sans-serif; font-weight: 200; font-size: 64px; line-height: 62px;
    color: var(--white); text-shadow: 0 0 3px rgba(0,0,0,.8);
    letter-spacing: -4px;
  }
  .entry .label {
    position: absolute; left: 245px; top: 0; height: 52px;
    border-left: 1.5px solid var(--white); padding-left: 9px; padding-top: 1px;
    color: var(--white); text-shadow: 0 2px 3px rgba(0,0,0,.6);
  }
  .entry .title { font-size: 24px; font-weight: 300; line-height: 26px; white-space: nowrap; letter-spacing: .2px; }
  .entry .sub { font-size: 18px; font-weight: 300; line-height: 22px; white-space: nowrap; color: var(--soft); }
  .brand-tab {
    position: absolute; left: 0; top: 853px; width: 330px; height: 81px;
    background: var(--white); border-radius: 0 8px 0 0;
  }
  .brand-tab .mark {
    position: absolute; left: 28px; top: 28px; width: 26px; height: 26px;
    background: var(--gold);
  }
  .brand-tab .name {
    position: absolute; left: 66px; top: 25px;
    font-size: 24px; font-weight: 400; color: var(--ink); letter-spacing: .5px;
  }
</style>
</head>
<body>
<main class="page">
  <div class="corner-glow corner-glow--top-right" role="img" aria-label="Gold angular accent"></div>
  <div class="corner-glow corner-glow--bottom-right" role="img" aria-label="Gold angular accent"></div>
  <div class="corner-glow corner-glow--bottom-left" role="img" aria-label="Gold angular accent"></div>

  <header class="index-banner"><h1>INDEX</h1></header>

  <section class="entry" style="left:54px;top:198px">
    <div class="thumb" role="img" aria-label="Company emblem on yellow" style="background:linear-gradient(90deg,#e7b820,#f0c83a)"></div>
    <span class="num">2</span>
    <div class="label"><div class="title">ABOUT OUR COMPANY</div><div class="sub">BRIGHTLINE ENERGY</div></div>
  </section>
  <section class="entry" style="left:54px;top:285px">
    <div class="thumb" role="img" aria-label="Collage of partner brand logos" style="background:linear-gradient(90deg,#e9e9e9,#ffffff)"></div>
    <span class="num">3</span>
    <div class="label"><div class="title">OUR BRANDS</div><div class="sub">QUALITY PRODUCTS</div></div>
  </section>
  <section class="entry" style="left:54px;top:371px">
    <div class="thumb" role="img" aria-label="Warehouse racks stocked with generators" style="background:linear-gradient(90deg,#9a9a96,#cfcfcb)"></div>
    <span class="num">4</span>
    <div class="label"><div class="title">OUR STOCK</div><div class="sub">LARGEST IN USA</div></div>
  </section>
  <section class="entry" style="left:54px;top:458px">
    <div class="thumb" role="img" aria-label="Standby diesel generator engine" style="background:linear-gradient(90deg,#1e1e1e,#3a3a3a 70%,#e6e6e6)"></div>
    <span class="num">5</span>
    <div class="label"><div class="title">STANDBY GENERATOS</div><div class="sub">DIESEL GENERATOR</div></div>
  </section>
  <section class="entry" style="left:54px;top:545px">
    <div class="thumb" role="img" aria-label="Prime diesel generator with open enclosure" style="background:linear-gradient(90deg,#e4e4e4,#2a2a2a 55%,#d8d8d8)"></div>
    <span class="num">6</span>
    <div class="label"><div class="title">PRIME GENERATOS</div><div class="sub">DIESEL GENERATOR</div></div>
  </section>
  <section class="entry" style="left:54px;top:632px">
    <div class="thumb" role="img" aria-label="Trailer-mounted rental generator" style="background:linear-gradient(90deg,#2b2b2b,#f0f0f0 45%,#dcdcdc)"></div>
    <span class="num">7</span>
    <div class="label"><div class="title">RENTAL GENERATOS</div><div class="sub">DIESEL GENERATOR</div></div>
  </section>

  <section class="entry" style="left:583px;top:198px">
    <div class="thumb" role="img" aria-label="AC alternator housing" style="background:linear-gradient(90deg,#4a4a4a,#1a1a1a)"></div>
    <span class="num">8</span>
    <div class="label"><div class="title">AC ALTERNATORS</div><div class="sub">ELECTRICAL GENERATOR</div></div>
  </section>
  <section class="entry" style="left:583px;top:285px">
    <div class="thumb" role="img" aria-label="Voltage regulator circuit boards" style="background:linear-gradient(90deg,#e8e8e8,#3c3c3c 40%,#f2f2f2 70%,#ffffff)"></div>
    <span class="num">9</span>
    <div class="label"><div class="title">ALTERNATOR PARTS</div><div class="sub">REAL POWER</div></div>
  </section>
  <section class="entry" style="left:583px;top:371px">
    <div class="thumb" role="img" aria-label="Generator controller panel with display" style="background:linear-gradient(90deg,#1a1a1a,#2e2e2e)"></div>
    <span class="num">10</span>
    <div class="label"><div class="title">CONTROLLERS</div><div class="sub">REAL POWER</div></div>
  </section>
  <section class="entry" style="left:583px;top:458px">
    <div class="thumb" role="img" aria-label="Automatic transfer switch cabinet" style="background:linear-gradient(90deg,#cfcfcf,#e6e6e6)"></div>
    <span class="num">11</span>
    <div class="label"><div class="title">TRANSFER SWITCHES</div><div class="sub">REAL POWER</div></div>
  </section>
  <section class="entry" style="left:583px;top:545px">
    <div class="thumb" role="img" aria-label="Distribution truck on the road" style="background:linear-gradient(90deg,#8a8a86,#3a2a2a 60%,#6e3a34)"></div>
    <span class="num">12</span>
    <div class="label"><div class="title">OUR DISTRIBUTORS</div><div class="sub">REAL POWER</div></div>
  </section>

  <footer class="brand-tab">
    <span class="mark"></span>
    <span class="name">Brightline Energy</span>
  </footer>
</main>
</body>
</html>
```